" Nome da empresa: Recanto Vivale CLINICA DE NUTRIÇAO SOMOS NUTRICIONISTAS E DESEJAMOS PROPORCIONAR AOS NOSSOS PACIENTES UM TRATAMENTO INDIVIDUALIZADO. FAREMOS ATENDIMENTOS NUTRICIONAIS A FIM DE LEVAR QUALIDADE DE VIDA E PREVENÇAO de doenças, focando na educaçao nutricional "

```html
<!DOCTYPE html>
<html lang="pt-BR">
<head>
<meta charset="utf-8">
<title>Recanto Vivale — Cartão de Visita</title>
<link rel="stylesheet" href="https://fonts.googleapis.com/css2?family=Quicksand:wght@500;600&family=Open+Sans:ital,wght@0,400;1,400&display=swap">
<style>
  :root {
    --bg: #ece8e2;
    --card-white: #ffffff;
    --card-green: #1d5a4a;
    --brand-green: #1f5b4b;
    --brand-orange: #e9a13b;
    --text-light: #ffffff;
    --text-muted: #cfe0d9;
  }
  html, body {
    margin: 0;
    width: 1200px;
    height: 1200px;
    overflow: hidden;
    background: var(--bg);
  }
  .canvas {
    position: relative;
    width: 1200px;
    height: 1200px;
  }
  .card {
    position: absolute;
    left: 273px;
    width: 652px;
    height: 410px;
    border-radius: 30px;
    box-sizing: border-box;
  }
  .card--front {
    top: 146px;
    background: var(--card-white);
    box-shadow: 0 2px 10px rgba(0,0,0,0.08);
  }
  .card--back {
    top: 598px;
    background: var(--card-green);
    box-shadow: 0 2px 10px rgba(0,0,0,0.12);
  }
  .brand {
    font-family: "Quicksand", sans-serif;
    font-weight: 600;
    color: var(--brand-green);
    margin: 0;
    white-space: nowrap;
  }
  .front-lockup {
    position: absolute;
    left: 0;
    right: 0;
    top: 195px;
    text-align: center;
  }
  .front-lockup .brand {
    font-size: 52px;
    line-height: 1;
    display: inline-flex;
    align-items: center;
    gap: 14px;
  }
  .brand-dot {
    width: 14px;
    height: 14px;
    border-radius: 50%;
    background: var(--brand-orange);
    display: inline-block;
  }
  .tagline {
    font-family: "Open Sans", sans-serif;
    color: var(--brand-orange);
    margin: 10px 0 0;
    font-size: 14px;
    letter-spacing: 0.2px;
  }
  .back-lockup {
    position: absolute;
    left: 48px;
    top: 80px;
  }
  .back-lockup .brand {
    color: var(--text-light);
    font-size: 24px;
    line-height: 1;
  }
  .back-lockup .tagline {
    color: var(--text-muted);
    font-size: 8px;
    margin-top: 5px;
  }
  .person {
    position: absolute;
    left: 357px;
    top: 102px;
    color: var(--text-light);
  }
  .person__name {
    font-family: "Open Sans", sans-serif;
    font-size: 25px;
    margin: 0;
    line-height: 1.1;
  }
  .person__role {
    font-family: "Open Sans", sans-serif;
    font-style: italic;
    font-size: 14px;
    margin: 4px 0 0 62px;
    color: var(--text-muted);
  }
  .contacts {
    position: absolute;
    left: 424px;
    top: 210px;
    margin: 0;
    padding: 0;
    list-style: none;
    font-family: "Open Sans", sans-serif;
    font-size: 11.5px;
    color: var(--text-light);
    line-height: 1.7;
  }
  .contacts li { margin-bottom: 6px; }
  .contacts .address { line-height: 1.35; }
</style>
</head>
<body>
<main class="canvas">
  <section class="card card--front" aria-label="Frente do cartão">
    <div class="front-lockup">
      <h1 class="brand"><span class="brand-dot"></span>Recanto Vivale</h1>
      <p class="tagline">Saúde-Ciência-Educação Nutricional</p>
    </div>
  </section>

  <section class="card card--back" aria-label="Verso do cartão">
    <div class="back-lockup">
      <p class="brand">Recanto Vivale</p>
      <p class="tagline">Saúde · Ciência · Educação Nutricional</p>
    </div>
    <div class="person">
      <p class="person__name">Nome Sobrenome</p>
      <p class="person__role">Função</p>
    </div>
    <ul class="contacts">
      <li>Tel:0000-0000</li>
      <li>Cel:0000-0000</li>
      <li>Email:contato@recantovivale.com.br</li>
      <li class="address">Endereço:Rua das Flores,00 Bairro<br>Jardins, Cidade das Flores</li>
    </ul>
  </section>
</main>
</body>
</html>
```